Tavenorix - world unique technology for better life - please let them know who am i at first sight

We need a new business card for company which is a provider of unique crystal based technology suitable for all living being. For more information and final design you can use our brochure (our colours are black and blue from brochure).
We use Verdana font

Industry/Entity Type

Business

Contact Information for Business Card

regular dimension

Font styles to use
Other font styles liked:
• Verdana

Requirements
Must have
• Logo
• name
• function/position
• phone
• mobile
• e-mail
• adress
Nice to have
• inovative design (technology directed)

```html
<!DOCTYPE html>
<html lang="en">
<head>
<meta charset="utf-8">
<title>Tavenorix Business Card</title>
<link rel="stylesheet" href="https://fonts.googleapis.com/css2?family=Noto+Sans:ital,wght@0,300;0,400;0,700;1,400&display=swap">
<style>
  :root {
    --bg: #9a9a98;
    --card-white: #f4f5f5;
    --blue: #1aa6de;
    --blue-deep: #0f8fcb;
    --blue-light: #33b6e8;
    --text-light: #ffffff;
    --shadow: rgba(0, 0, 0, 0.28);
  }
  * { box-sizing: border-box; margin: 0; padding: 0; }
  html, body {
    width: 1200px;
    height: 1000px;
    overflow: hidden;
    background: var(--bg);
    font-family: "Noto Sans", Verdana, sans-serif;
  }
  .canvas { position: relative; width: 1200px; height: 1000px; }

  .card {
    position: absolute;
    width: 700px;
    height: 400px;
    overflow: hidden;
    box-shadow: 0 8px 24px var(--shadow);
  }

  /* Front */
  .card--front {
    left: 420px;
    top: 70px;
    background: linear-gradient(135deg, var(--blue-light), var(--blue-deep));
    display: flex;
    align-items: center;
    justify-content: center;
  }
  .brand { display: flex; align-items: center; gap: 22px; color: var(--text-light); }
  .brand__dot { border-radius: 50%; background: var(--text-light); flex: none; }
  .brand__name {
    font-weight: 300;
    letter-spacing: 0.04em;
    text-transform: uppercase;
    white-space: nowrap;
  }
  .card--front .brand__dot { width: 96px; height: 96px; }
  .card--front .brand__name { font-size: 58px; }

  /* Back */
  .card--back {
    left: 80px;
    top: 530px;
    background: var(--card-white);
    color: var(--text-light);
  }
  .back__panel {
    position: absolute;
    left: 385px;
    top: 0;
    width: 315px;
    height: 100%;
    background: linear-gradient(160deg, var(--blue-light), var(--blue-deep));
  }
  .card--back .brand { position: absolute; left: 405px; top: 52px; gap: 12px; }
  .card--back .brand__dot { width: 48px; height: 48px; }
  .card--back .brand__name { font-size: 31px; }

  .band {
    position: absolute;
    background: var(--blue);
    display: flex;
    align-items: center;
    white-space: nowrap;
  }
  .band--name {
    left: 0; top: 32px; width: 385px; height: 78px;
    flex-direction: column; justify-content: center; align-items: flex-end;
    padding-right: 65px;
  }
  .person__name { font-weight: 700; font-size: 25px; line-height: 1.1; }
  .person__role { font-style: italic; font-size: 18px; }

  .band--contact { height: 46px; padding-left: 20px; font-size: 17px; }
  .band--phone  { left: 125px; top: 132px; width: 247px; }
  .band--mobile { left: 85px;  top: 188px; width: 287px; }
  .band--email  { left: 20px;  top: 244px; width: 352px; }
  .band--address {
    left: 0; top: 305px; width: 372px; height: 56px;
    padding-left: 20px; font-size: 17px;
  }
</style>
</head>
<body>
<div class="canvas">

  <section class="card card--front" aria-label="Business card front">
    <div class="brand">
      <span class="brand__dot"></span>
      <span class="brand__name">Tavenorix</span>
    </div>
  </section>

  <section class="card card--back" aria-label="Business card back">
    <div class="back__panel"></div>
    <div class="brand">
      <span class="brand__dot"></span>
      <span class="brand__name">Tavenorix</span>
    </div>

    <div class="band band--name">
      <span class="person__name">Your Name</span>
      <span class="person__role">Position</span>
    </div>
    <div class="band band--contact band--phone">Phone : 012- 345- 6789</div>
    <div class="band band--contact band--mobile">Mobile : 098- 765- 4321</div>
    <div class="band band--contact band--email">Email : yourname@tavenorix.example</div>
    <div class="band band--address">Address which you want to provide</div>
  </section>

</div>
</body>
</html>
```